Harwick Lending Hard Money Lender

We are looking for this flyer to be redesigned. We would like it to be even more simple than the attached design. No photos, no exclamation points, a 3-4 color palate maximum. We would do not want any graphics around the "Harwick Lending" logo.

```html
<!DOCTYPE html>
<html lang="en">
<head>
<meta charset="utf-8">
<title>Harwick Lending – Hard Money Loans</title>
<link href="https://fonts.googleapis.com/css2?family=Montserrat:ital,wght@0,400;0,500;0,800;1,800&display=swap" rel="stylesheet">
<style>
  :root {
    --page: #e4e4e4;
    --flyer-top: #4a82aa;
    --flyer-bottom: #7ab4d0;
    --corner-top: #97bbd0;
    --corner-bottom: #c3d8e3;
    --navy: #27245e;
    --ink: #111111;
    --light: #eef4f8;
  }
  html, body {
    margin: 0;
    padding: 0;
    width: 1200px;
    height: 1000px;
    overflow: hidden;
    background: var(--page);
    font-family: "Montserrat", sans-serif;
  }
  .flyer {
    position: absolute;
    left: 252px;
    top: 50px;
    width: 697px;
    height: 900px;
    background: linear-gradient(to bottom, var(--flyer-top) 0%, var(--flyer-bottom) 100%);
    overflow: hidden;
    color: var(--navy);
  }
  .flyer-corners {
    position: absolute;
    inset: 0;
  }
  .flyer > p, .flyer > h1, .flyer > h2, .flyer > ul {
    margin: 0;
    position: absolute;
    line-height: 1;
  }
  .brand-name {
    left: 0;
    width: 100%;
    top: 118px;
    text-align: center;
    font-size: 46px;
    font-weight: 500;
    color: var(--ink);
    letter-spacing: 1px;
  }
  .headline {
    left: 48px;
    top: 285px;
    font-size: 49px;
    font-weight: 800;
    letter-spacing: 0.5px;
  }
  .rate-note {
    right: 60px;
    top: 331px;
    font-size: 16px;
    font-weight: 400;
    color: var(--light);
    letter-spacing: 0.5px;
  }
  .benefits {
    left: 47px;
    top: 434px;
    padding: 0;
    list-style: none;
    font-size: 21px;
    font-weight: 400;
    letter-spacing: 0.4px;
  }
  .benefits li { height: 44px; }
  .benefits small { font-size: 13px; }
  .contact-title {
    left: 47px;
    top: 663px;
    font-size: 36px;
    font-weight: 800;
    letter-spacing: 1px;
  }
  .contact-line {
    left: 48px;
    font-size: 16px;
    font-weight: 400;
    letter-spacing: 0.4px;
  }
  .contact-email { top: 712px; }
  .contact-web { top: 745px; }
  .contact-address {
    top: 778px;
    font-size: 11px;
    letter-spacing: 0.2px;
  }
  .contact-address span { margin-left: 10px; }
  .phone {
    right: 48px;
    top: 811px;
    font-size: 56px;
    font-weight: 800;
    font-style: italic;
    letter-spacing: 0.5px;
  }
</style>
</head>
<body>
  <main class="flyer">
    <svg class="flyer-corners" width="697" height="900" viewBox="0 0 697 900" aria-hidden="true">
      <polygon points="0,0 62,0 0,72" fill="var(--corner-top)"/>
      <polygon points="697,830 637,900 697,900" fill="var(--corner-bottom)"/>
    </svg>

    <p class="brand-name">HARWICK LENDING</p>

    <h1 class="headline">HARD MONEY LOANS</h1>
    <p class="rate-note">Rates From 8%</p>

    <ul class="benefits">
      <li>Same-Day Approval</li>
      <li>No Processing, Appraisal, or Extra Fees</li>
      <li>100% Financing <small>(w/ Additional Collateral)</small></li>
    </ul>

    <h2 class="contact-title">CONTACT US:</h2>
    <p class="contact-line contact-email">hello@harwicklending.com</p>
    <p class="contact-line contact-web">http://harwicklending.com</p>
    <p class="contact-line contact-address">1480 Alder Ridge Way, Suite 210<span>Denver, CO 80231</span></p>

    <p class="phone">303.555.0147</p>
  </main>
</body>
</html>
```